Zielgruppe
Wir verkaufen spezielle Teemischungen an Frauen, die schwanger werden möchten und sich gezielt ein Mädchen oder einen Jungen wünschen. Die Rezeptur unseres Tees, ist speziell auf den jeweiligen Wunsch abgestimmt. Wir verkaufen daher einen Sonnenwiese Tee und einen Bergquelle Tee.
Aufgabenstellung
Wir benötigen ein Etikett Design für den Sonnenwiese Tee. Wenn das Etikett fertig designed wurde, würden wir gerne anschließend ein Etikett für den Bergquelle Tee designen lassen. Das Design sollte klar, hochwertig und modern wirken. Es sollte erkennbar sein, dass der Tee speziell für Frauen mit einem Mädchenwunsch ist. Die Hintergrundfarbe des Designes bzw. des Etiketts sollte in zart rosa sein.

```html
<!DOCTYPE html>
<html lang="de">
<head>
<meta charset="utf-8">
<title>Sonnenwiese Tee – Etikett</title>
<link rel="stylesheet" href="https://fonts.googleapis.com/css2?family=Fira+Sans:wght@400;500;700&family=Great+Vibes&display=swap">
<style>
  :root {
    --bg: #fcebf0;
    --rose: #ee92b0;
    --rose-soft: #f5b6c8;
    --rose-mark: #f7c9d6;
    --grey-band: #d9d4d6;
    --grey-text: #6d6466;
    --ink: #1d1a1b;
  }
  * { margin: 0; padding: 0; box-sizing: border-box; }
  html, body { width: 846px; height: 1200px; overflow: hidden; background: var(--bg); }
  .label {
    position: relative; width: 846px; height: 1200px;
    background: var(--bg); overflow: hidden;
    font-family: "Fira Sans", sans-serif; color: var(--ink);
  }

  .floral { position: absolute; border-radius: 46% 54% 50% 50%; }
  .floral--top-left { left: -70px; top: -60px; width: 260px; height: 380px;
    background: radial-gradient(ellipse at 45% 35%, #f7dde5 0%, #f0c2d1 38%, #e3d8dc 56%, rgba(252,235,240,0) 74%); }
  .floral--top-right { right: -60px; top: -50px; width: 290px; height: 300px;
    background: radial-gradient(ellipse at 55% 35%, #f2aec4 0%, #f5cbd7 40%, #efe0d6 58%, rgba(252,235,240,0) 74%); }
  .floral--bottom-left { left: -50px; bottom: -50px; width: 260px; height: 290px;
    background: radial-gradient(ellipse at 45% 55%, #f1b9cb 0%, #ecd3d4 40%, #dbe3dc 56%, rgba(252,235,240,0) 74%); }
  .floral--bottom-right { right: -60px; bottom: -60px; width: 300px; height: 280px;
    background: radial-gradient(ellipse at 55% 55%, #f4eeee 0%, #e6dede 30%, #cfe0dc 50%, rgba(252,235,240,0) 74%); }

  .brand-mark {
    position: absolute; left: 328px; top: 40px; width: 190px; height: 190px;
    border-radius: 50%; background: var(--rose-mark);
  }
  .brand {
    position: absolute; left: 0; width: 846px; top: 246px;
    text-align: center; font-size: 56px; line-height: 1; font-weight: 400;
    color: var(--rose-soft); letter-spacing: 2px;
  }
  .product-name {
    position: absolute; left: 0; width: 846px; top: 310px;
    text-align: center; font-family: "Great Vibes", cursive; font-weight: 400;
    font-size: 92px; line-height: 1; color: var(--rose);
  }
  .product-type {
    position: absolute; left: 0; width: 846px; top: 374px; padding-left: 10px;
    text-align: center; font-family: "Great Vibes", cursive;
    font-size: 84px; line-height: 1; color: var(--grey-text);
  }
  .tagline { position: absolute; left: 0; top: 440px; width: 846px; height: 170px; overflow: visible; }
  .tagline text { font-family: "Great Vibes", cursive; font-size: 36px; fill: var(--ink); }

  .illustration {
    position: absolute; left: 214px; top: 520px; width: 420px; height: 380px;
    border-radius: 44% 56% 48% 52% / 40% 46% 54% 60%;
    background:
      radial-gradient(ellipse at 62% 18%, rgba(150,90,80,.35) 0%, rgba(150,90,80,0) 18%),
      radial-gradient(ellipse at 50% 32%, #f6d2d2 0%, rgba(246,210,210,0) 30%),
      radial-gradient(ellipse at 40% 80%, #f3a9c0 0%, rgba(243,169,192,0) 24%),
      radial-gradient(ellipse at 20% 62%, #f8f4f2 0%, rgba(248,244,242,0) 22%),
      radial-gradient(ellipse at 80% 62%, #f8f4f2 0%, rgba(248,244,242,0) 22%),
      radial-gradient(ellipse at 50% 50%, #f1d3d6 0%, #f4e0e2 55%, rgba(252,235,240,0) 76%);
  }

  .bands { position: absolute; left: 0; top: 880px; width: 846px; height: 230px; }
  .bands .band--rose { fill: var(--rose-soft); opacity: .9; }
  .bands .band--grey { fill: var(--grey-band); opacity: .9; }
  .bands text { font-family: "Fira Sans", sans-serif; fill: var(--ink); font-size: 24px; }

  .storage {
    position: absolute; left: 0; width: 846px; top: 1076px;
    text-align: center; font-size: 15px; line-height: 26px;
  }
  .net-weight {
    position: absolute; left: 0; width: 846px; top: 1143px;
    text-align: center; font-size: 20px;
  }

  .ingredients {
    position: absolute; left: 22px; top: 1152px;
    transform-origin: 0 0; transform: rotate(-90deg);
    font-size: 15px; line-height: 24px; white-space: nowrap; width: 1130px;
  }
  .maker {
    position: absolute; left: 818px; top: 224px;
    transform-origin: 0 0; transform: rotate(90deg);
    font-size: 19px; white-space: nowrap; letter-spacing: .6px;
  }
  .maker span { margin-right: 22px; }
  .website {
    position: absolute; left: 815px; top: 896px;
    transform-origin: 0 0; transform: rotate(90deg);
    font-size: 20px; font-weight: 700; white-space: nowrap;
  }
</style>
</head>
<body>
<main class="label">
  <div class="floral floral--top-left" role="img" aria-label="Aquarell-Blüten und Baumwollkapseln in Rosa"></div>
  <div class="floral floral--top-right" role="img" aria-label="Aquarell-Pfingstrosen in Rosa mit Zweigen"></div>
  <div class="floral floral--bottom-left" role="img" aria-label="Aquarell-Blüten mit Blättern"></div>
  <div class="floral floral--bottom-right" role="img" aria-label="Baumwollkapseln und Blätter in Aquarell"></div>

  <div class="brand-mark"></div>
  <div class="brand">Lunavio</div>
  <h1 class="product-name">Sonnenwiese</h1>
  <div class="product-type">Tee</div>

  <svg class="tagline" viewBox="0 0 846 170" aria-label="spezielle Rezeptur bei bestehendem Mädchenwunsch">
    <path id="tagline-arc" d="M118 160 Q420 -66 730 160" fill="none"/>
    <text><textPath href="#tagline-arc" startOffset="50%" text-anchor="middle">spezielle Rezeptur bei bestehendem Mädchenwunsch</textPath></text>
  </svg>

  <div class="illustration" role="img" aria-label="Aquarell-Illustration eines schlafenden Babys zwischen Blüten und Baumwolle"></div>

  <svg class="bands" viewBox="0 0 846 230">
    <polygon class="band--grey" points="440,21 757,46 740,110 457,76"/>
    <polygon class="band--rose" points="114,42 540,25 510,88 126,108"/>
    <polygon class="band--grey" points="165,76 398,50 431,127 169,207"/>
    <polygon class="band--rose" points="470,50 727,80 723,203 508,135"/>
    <text transform="translate(140 92) rotate(-7)">Premium Qualität</text>
    <text transform="translate(563 42) rotate(6)" letter-spacing="1.5">Glutenfrei</text>
    <text transform="translate(232 135) rotate(-13)">100% natürlich</text>
    <text transform="translate(180 176) rotate(-13)">aus kontrolliertem Anbau</text>
    <text transform="translate(528 86) rotate(15)">enthält Matcha</text>
    <text transform="translate(562 138) rotate(12)" font-size="28">vegan</text>
  </svg>

  <p class="storage">Kühl und trocken lagern.<br>Mindestens haltbar bis: Siehe Etikett</p>
  <p class="net-weight">Nettogewicht 75 g</p>

  <div class="ingredients">
    <p>Zutaten: Frauenmantelkraut*, Brennnesselblätter*, Schafgarbe*, Rosmarin*, Apfelstücke*, Hibiskusblüten*, Basilikum*, Holunderblüten*, Eisenkraut*, Matcha.</p>
    <p>Zubereitung: 1-2 Teelöffel pro Tasse (200 ml) bei 100°C 4-6 Minuten lang ziehen lassen.</p>
  </div>

  <div class="maker"><span>Lunavio GmbH</span><span>Lindenweg 24</span><span>52311 Talbrück</span><span>info@lunavio.de</span></div>
  <div class="website">www.lunavio.de</div>
</main>
</body>
</html>
```